Creation of a book cover
Size : 14 x 20,5 cm (+ 5 mm bleed area at the top, bottom and right areas)
The Title is a French sentence which means “The heron dreaming on the cold roof of this empty station”. It’s a surrealistic title which has no link to the story.
AUTHOR : Mathieu Vorlange
TITLE : "Le héron rêvant sur le toit froid de cette gare vide »
PUBLISHER (AT THE BOTTOM OF THE PAGE) : Editions Parvenche
I send a PDF file with the kind of cover we have imagine, but you can propose something different. The glass and the fly can of course be used.

```html
<!DOCTYPE html>
<html lang="fr">
<head>
<meta charset="utf-8">
<title>Le héron rêvant sur le toit froid de cette gare vide — Mathieu Vorlange</title>
<link href="https://fonts.googleapis.com/css2?family=Bebas+Neue&family=Montserrat:wght@700&family=Permanent+Marker&display=swap" rel="stylesheet">
<style>
  :root {
    --backdrop: #242526;
    --cover-light: #dfe2e7;
    --cover-mid: #cdd1d7;
    --cover-shade: #b7bcc4;
    --ink: #2f3a40;
    --blood: #c8202a;
    --blood-deep: #a3121c;
    --glass-light: #eef0f2;
    --glass-tone: #9ea6ab;
  }
  * { margin: 0; padding: 0; box-sizing: border-box; }
  html, body {
    width: 1200px;
    height: 973px;
    overflow: hidden;
    background: var(--backdrop);
  }
  .book-cover {
    position: absolute;
    left: 295px;
    top: 44px;
    width: 610px;
    height: 885px;
    background: linear-gradient(160deg, var(--cover-light) 0%, var(--cover-mid) 55%, var(--cover-shade) 100%);
    overflow: hidden;
  }
  .author {
    position: absolute;
    top: 42px;
    left: 0;
    width: 570px;
    text-align: center;
    font-family: 'Montserrat', sans-serif;
    font-weight: 700;
    font-size: 17px;
    color: var(--ink);
    letter-spacing: 0.2px;
  }
  .splatter-art {
    position: absolute;
    left: 128px;
    top: 18px;
    width: 482px;
    height: 330px;
    background: radial-gradient(ellipse at 68% 42%, rgba(200, 32, 42, 0.55) 0%, rgba(200, 32, 42, 0.22) 38%, rgba(200, 32, 42, 0) 70%);
  }
  .title-main {
    position: absolute;
    left: 0;
    width: 610px;
    text-align: center;
    font-family: 'Permanent Marker', cursive;
    color: var(--blood);
    line-height: 1;
    transform: rotate(-4deg);
  }
  .title-main--first {
    top: 232px;
    left: -40px;
    font-size: 92px;
  }
  .title-main--second {
    top: 312px;
    font-size: 108px;
  }
  .title-rest {
    position: absolute;
    left: 0;
    width: 610px;
    text-align: center;
    font-family: 'Bebas Neue', sans-serif;
    font-size: 46px;
    color: var(--ink);
    line-height: 1;
    letter-spacing: 0.5px;
  }
  .title-rest--first { top: 424px; }
  .title-rest--second { top: 480px; }
  .glass-art {
    position: absolute;
    left: 212px;
    top: 565px;
    width: 180px;
    height: 215px;
    background: linear-gradient(180deg, var(--glass-light) 0%, var(--glass-tone) 100%);
    border-radius: 10px;
  }
  .publisher {
    position: absolute;
    top: 812px;
    left: 0;
    width: 610px;
    text-align: center;
    font-family: 'Montserrat', sans-serif;
    font-weight: 700;
    font-size: 18px;
    color: var(--ink);
  }
</style>
</head>
<body>
  <main class="book-cover">
    <p class="author">Mathieu Vorlange</p>
    <div class="splatter-art" role="img" aria-label="Éclaboussures rouges et trace circulaire de verre couleur sang"></div>
    <h1>
      <span class="title-main title-main--first">LE</span>
      <span class="title-main title-main--second">HÉRON</span>
      <span class="title-rest title-rest--first">RÊVANT SUR LE TOIT FROID</span>
      <span class="title-rest title-rest--second">DE CETTE GARE VIDE</span>
    </h1>
    <div class="glass-art" role="img" aria-label="Illustration d’un verre d’eau avec une mouche posée sur le bord"></div>
    <p class="publisher">Editions Parvenche</p>
  </main>
</body>
</html>
```